Book Cover

Hello!
I need someone to design a book cover with the title, subtitle and one of the photos attached.

- Title: Beyond the Grey Hours - By Corwin Ashdale
- Subtitle: A Steady Handbook for finding calm and strength after hard news.

```html
<!DOCTYPE html>
<html lang="en">
<head>
<meta charset="UTF-8">
<title>Beyond the Grey Hours — Book Cover</title>
<link rel="stylesheet" href="https://fonts.googleapis.com/css2?family=Josefin+Sans:wght@400;600;700&family=Mr+Dafoe&display=swap">
<style>
  :root {
    --ink: #07080c;
    --navy: #151b2e;
    --sky: #cfe0ee;
    --sky-deep: #9fbbd3;
    --gold: #f1c58e;
    --white: #ffffff;
  }
  * { margin: 0; padding: 0; box-sizing: border-box; }
  html, body {
    width: 854px;
    height: 1200px;
    overflow: hidden;
    background: var(--ink);
  }
  .cover {
    position: relative;
    width: 854px;
    height: 1200px;
    overflow: hidden;
    background: var(--ink);
  }
  .cover-photo {
    position: absolute;
    inset: 0;
    background:
      radial-gradient(ellipse 42% 30% at 50% 38%, rgba(233, 196, 170, 0.85), rgba(233, 196, 170, 0) 70%),
      radial-gradient(ellipse 30% 22% at 18% 20%, rgba(255, 246, 228, 0.9), rgba(255, 246, 228, 0) 70%),
      radial-gradient(ellipse 25% 40% at 10% 55%, rgba(120, 96, 70, 0.55), rgba(120, 96, 70, 0) 70%),
      linear-gradient(180deg, var(--sky) 0%, var(--sky-deep) 40%, #4a4f63 60%, var(--navy) 72%, var(--ink) 82%);
  }
  .cover-shade {
    position: absolute;
    left: 0; right: 0; bottom: 0;
    height: 520px;
    background: linear-gradient(180deg, rgba(7, 8, 12, 0) 0%, rgba(7, 8, 12, 0.85) 45%, var(--ink) 70%);
  }
  .title-block {
    position: absolute;
    left: 0; right: 0;
    top: 790px;
    height: 230px;
    text-align: center;
    font-weight: normal;
  }
  .title-script {
    position: absolute;
    left: 0; right: 0;
    top: 0;
    font-family: "Mr Dafoe", cursive;
    font-size: 116px;
    line-height: 1.2;
    color: var(--gold);
    z-index: 2;
    transform: rotate(-3deg);
  }
  .title-main {
    position: absolute;
    left: 0; right: 0;
    top: 160px;
    font-family: "Josefin Sans", sans-serif;
    font-weight: 700;
    font-size: 70px;
    line-height: 1;
    letter-spacing: 1px;
    color: var(--white);
    z-index: 1;
  }
  .subtitle {
    position: absolute;
    left: 0; right: 0;
    top: 1036px;
    text-align: center;
    font-family: "Josefin Sans", sans-serif;
    font-weight: 600;
    font-size: 20px;
    line-height: 1.4;
    letter-spacing: 0.5px;
    text-transform: uppercase;
    color: var(--white);
  }
  .author {
    position: absolute;
    left: 0; right: 0;
    top: 1118px;
    text-align: center;
    font-family: "Josefin Sans", sans-serif;
    font-weight: 700;
    font-size: 32px;
    letter-spacing: 8px;
    text-transform: uppercase;
    color: var(--gold);
  }
</style>
</head>
<body>
  <main class="cover">
    <div class="cover-photo" role="img" aria-label="Portrait photograph of an older man with grey hair and beard looking upward in soft winter sunlight"></div>
    <div class="cover-shade"></div>
    <h1 class="title-block">
      <span class="title-script">Beyond the</span>
      <span class="title-main">GREY HOURS</span>
    </h1>
    <p class="subtitle">A Steady Handbook for finding calm<br>and strength after hard news.</p>
    <p class="author">By Corwin Ashdale</p>
  </main>
</body>
</html>
```